Psychometric Assessment Flyer/Brochure Makeover

TORVEN Consulting is an organisational psychology and human resource management consulting firm based in Melbourne, Australia (www.torvenadvise.com.au). We offer a range of organisational development and executive recruitment services, however the largest part of our business is our online psychometric assessments portal, which is currently used by hundreds of organisations Australia wide as part of their recruitment process.

We are seeking assistance with the redevelopment of an existing 2-page (1 x A4 page double sided) brochure/flyer to make it more impactful. The main purpose of the brochure is to increase sales revenue in our assessments area. We believe that part of the path to increasing/generating revenue is going to be caused by enquiries made to the business as a result of reading this flyer.

Due to the complex nature of psychometric assessments, the content in this existing brochure attached needs to be simplified and easy to understand. Our target audience are businesses and organisations from a range of sectors (eg. not-for-profit/commercial/local & state government). Feel free if you just want to capture key points also.

Please note, we are not just seeking an aesthetic improvement to the brochure, we are seeking direction on the layout and content also.

Target Market(s)

HR Managers, Recruiters, CEO, General Manager, Mangers of private and not for profit organisations.

Font styles to use
Sans Serif

Requirements
Must have
• Company logo (attached); colours are Dark Blue: R53 G67 B113, White: R255 G255 B 255. TORVEN Consulting also uses the following colours for corporate branding and communications:
• Dark Blue: R53 G67 B113 = Hex #354371
• Pink: R202 G48 B146 = Hex #CA3092
• Medium Blue: R80 G145 B205 = Hex #5091CD
• Yellow: R231, G166, B20 = Hex #E7A614
• Contact details as specified in attached flyer.

```html
<!DOCTYPE html>
<html lang="en">
<head>
<meta charset="utf-8">
<title>TORVEN Consulting – Psychometric Assessments Flyer</title>
<link href="https://fonts.googleapis.com/css2?family=Open+Sans:wght@400;600;700;800&family=Oswald:wght@400;500&display=swap" rel="stylesheet">
<style>
:root{
  --navy:#354371;
  --navy-deep:#1f2a4d;
  --mid-blue:#5091cd;
  --ink:#4a4f5c;
  --muted:#6b7080;
  --white:#ffffff;
  --paper:#ffffff;
  --backdrop:#dcd9d5;
  --photo-a:#2b3a63;
  --photo-b:#101a33;
}
*{box-sizing:border-box;margin:0;padding:0}
html,body{width:1200px;height:777px;overflow:hidden;background:var(--backdrop);font-family:"Open Sans",Arial,sans-serif;color:var(--ink)}
.page{position:absolute;top:52px;width:520px;height:673px;background:var(--paper);box-shadow:0 6px 18px rgba(0,0,0,.25);overflow:hidden}
.page--front{left:60px}
.page--back{left:620px}
.header{position:absolute;left:0;top:0;width:520px;height:270px}
.header svg{position:absolute;left:0;top:0}
.brand{position:absolute;left:18px;top:34px;font-weight:800;font-size:25px;letter-spacing:.5px;line-height:1.05;color:var(--navy)}
.brand--light{color:var(--white)}
.title{position:absolute;right:14px;top:22px;font-size:19px;font-weight:600;color:var(--white)}
.title--dark{color:var(--navy)}
.photo-label{position:absolute;left:0;top:75px;width:520px;height:185px}
.section{position:absolute;left:18px;right:16px}
.h-condensed{font-family:"Oswald",Arial,sans-serif;font-weight:500;font-size:14px;color:var(--navy);letter-spacing:.2px}
.h-sub{font-weight:700;font-size:10.5px;color:var(--navy)}
.body{font-size:8.2px;line-height:1.45;color:var(--muted)}
.benefits{position:absolute;left:18px;right:14px;top:366px;height:128px;border:1.2px solid var(--mid-blue);border-radius:7px}
.benefits__title{position:absolute;top:-10px;left:50%;transform:translateX(-50%);background:var(--paper);padding:0 12px;font-family:"Oswald",Arial,sans-serif;font-size:13px;color:var(--mid-blue);white-space:nowrap}
.benefits__intro{text-align:center;font-size:8px;line-height:1.45;color:var(--ink);margin:14px 20px 0}
.benefits__grid{display:grid;grid-template-columns:240px 1fr;row-gap:3.5px;margin:8px 0 0 10px}
.benefit{display:flex;align-items:center;font-size:8.2px;color:var(--ink);gap:5px}
.benefit__dot{width:13px;height:13px;border-radius:50%;background:var(--mid-blue);flex:none}
.note{position:absolute;left:60px;right:60px;top:510px;text-align:center;font-size:5.6px;line-height:1.4;color:var(--muted)}
.checks{display:grid;grid-template-columns:182px 126px 1fr;row-gap:2.5px;margin-top:8px}
.check{display:flex;align-items:center;gap:5px;font-size:8.2px;color:var(--ink)}
.footer{position:absolute;left:0;bottom:0;width:520px;height:36px}
.footer svg{position:absolute;left:0;top:0}
.footer__cta{position:absolute;left:17px;top:11px;font-size:11px;color:var(--white)}
.footer__url{position:absolute;right:20px;top:9px;font-size:13px;font-weight:700;color:var(--white)}
.col{position:absolute;top:284px;font-size:8.2px}
.col--left{left:18px;width:237px}
.col--right{left:273px;width:232px}
.col .body{text-align:justify;margin-top:2px}
.quote{position:absolute;left:18px;right:14px;top:398px}
.quote__head{display:flex;align-items:center;gap:3px;font-size:10.5px;font-weight:600;color:var(--mid-blue)}
.quote__mark{font-size:24px;font-weight:800;line-height:.7;color:var(--mid-blue)}
.quote .body{font-size:7.3px;line-height:1.5;margin-top:3px}
.quote ul{list-style:none;margin-top:4px}
.quote li{font-size:7.3px;line-height:1.5;color:var(--muted)}
.quote li::before{content:"• "}
</style>
</head>
<body>

<!-- FRONT PAGE -->
<section class="page page--front">
  <div class="header">
    <svg width="520" height="270" viewBox="0 0 520 270">
      <defs>
        <linearGradient id="photoFront" x1="0" y1="0" x2="1" y2="1">
          <stop offset="0" stop-color="var(--photo-b)"/>
          <stop offset=".55" stop-color="var(--photo-a)"/>
          <stop offset="1" stop-color="var(--photo-b)"/>
        </linearGradient>
      </defs>
      <path d="M0 72 H520 V238 Q260 268 0 238 Z" fill="url(#photoFront)"/>
      <path d="M0 238 Q260 268 520 238 V243 Q260 274 0 243 Z" fill="var(--mid-blue)"/>
      <polygon points="248,0 520,0 520,70 250,70 240,80" fill="var(--navy)"/>
      <polygon points="0,0 275,0 200,116 0,116" fill="var(--white)"/>
      <polygon points="275,0 283,0 208,116 200,116" fill="#c9cdd8"/>
    </svg>
    <div class="photo-label" role="img" aria-label="Photo of a businessman's cupped hands holding a cluster of people icons"></div>
    <div class="brand">TORVEN<br>Consulting</div>
    <div class="title">Psychometric Assessments</div>
  </div>

  <div class="section" style="top:275px">
    <h2 class="h-condensed">REDUCE HIRING MISTAKES</h2>
    <p class="body" style="margin-top:4px">Psychometric Assessments are a powerful and cost-effective way of accurately predicting the likelihood of success of a candidate in any given role. In comparison to traditional recruitment and selection processes such as interviews and reference checking, Psychometric Assessment is evidence based, unbiased and incredibly accurate.<br>The most accurate predictor of on the job success.</p>
  </div>

  <div class="benefits">
    <div class="benefits__title">BENEFITS OF ASSESSMENT</div>
    <p class="benefits__intro">The use of Psychometric Assessments in a recruitment process has led to substantial and sustained work outcomes including:</p>
    <div class="benefits__grid">
      <div class="benefit"><span class="benefit__dot"></span>Increased productivity and speed to productivity</div>
      <div class="benefit"><span class="benefit__dot"></span>Lower turnover</div>
      <div class="benefit"><span class="benefit__dot"></span>Less negative behaviours in the workplace</div>
      <div class="benefit"><span class="benefit__dot"></span>Less time invested recruiting &amp; training new employees</div>
      <div class="benefit"><span class="benefit__dot"></span>Improved employee engagement</div>
      <div class="benefit"><span class="benefit__dot"></span>Less money spent on advertising vacancies</div>
      <div class="benefit"><span class="benefit__dot"></span>Less disciplinary action required</div>
      <div class="benefit"><span class="benefit__dot"></span>Higher client satisfaction ratings</div>
    </div>
  </div>

  <p class="note">Please turn over to see a testimonial from Harlow Grove Care outlining the benefits they have experienced since implementing psychometric assessments as part of their recruitment process</p>

  <div class="section" style="top:528px">
    <h3 class="h-sub">What assessments can I administer?</h3>
    <p class="body" style="margin-top:2px">TORVEN offers a range of psychometric assessments designed to measure the likelihood of success at work,<br>as well as potential risk areas. These include:</p>
    <div class="checks">
      <div class="check"><svg width="9" height="9" viewBox="0 0 10 10"><circle cx="5" cy="5" r="4.3" fill="none" stroke="var(--mid-blue)" stroke-width="1"/><path d="M3 5.2l1.4 1.4L7 3.8" fill="none" stroke="var(--mid-blue)" stroke-width="1.1"/></svg>Personality</div>
      <div class="check"><svg width="9" height="9" viewBox="0 0 10 10"><circle cx="5" cy="5" r="4.3" fill="none" stroke="var(--mid-blue)" stroke-width="1"/><path d="M3 5.2l1.4 1.4L7 3.8" fill="none" stroke="var(--mid-blue)" stroke-width="1.1"/></svg>Values</div>
      <div class="check"><svg width="9" height="9" viewBox="0 0 10 10"><circle cx="5" cy="5" r="4.3" fill="none" stroke="var(--mid-blue)" stroke-width="1"/><path d="M3 5.2l1.4 1.4L7 3.8" fill="none" stroke="var(--mid-blue)" stroke-width="1.1"/></svg>Cognitive Ability</div>
      <div class="check"><svg width="9" height="9" viewBox="0 0 10 10"><circle cx="5" cy="5" r="4.3" fill="none" stroke="var(--mid-blue)" stroke-width="1"/><path d="M3 5.2l1.4 1.4L7 3.8" fill="none" stroke="var(--mid-blue)" stroke-width="1.1"/></svg>Emotional Intelligence</div>
      <div class="check"><svg width="9" height="9" viewBox="0 0 10 10"><circle cx="5" cy="5" r="4.3" fill="none" stroke="var(--mid-blue)" stroke-width="1"/><path d="M3 5.2l1.4 1.4L7 3.8" fill="none" stroke="var(--mid-blue)" stroke-width="1.1"/></svg>Resilience</div>
      <div class="check"><svg width="9" height="9" viewBox="0 0 10 10"><circle cx="5" cy="5" r="4.3" fill="none" stroke="var(--mid-blue)" stroke-width="1"/><path d="M3 5.2l1.4 1.4L7 3.8" fill="none" stroke="var(--mid-blue)" stroke-width="1.1"/></svg>Attitudes Toward Diversity</div>
      <div class="check"><svg width="9" height="9" viewBox="0 0 10 10"><circle cx="5" cy="5" r="4.3" fill="none" stroke="var(--mid-blue)" stroke-width="1"/><path d="M3 5.2l1.4 1.4L7 3.8" fill="none" stroke="var(--mid-blue)" stroke-width="1.1"/></svg>Engagement</div>
      <div class="check"><svg width="9" height="9" viewBox="0 0 10 10"><circle cx="5" cy="5" r="4.3" fill="none" stroke="var(--mid-blue)" stroke-width="1"/><path d="M3 5.2l1.4 1.4L7 3.8" fill="none" stroke="var(--mid-blue)" stroke-width="1.1"/></svg>OH&amp;S</div>
      <div class="check"><svg width="9" height="9" viewBox="0 0 10 10"><circle cx="5" cy="5" r="4.3" fill="none" stroke="var(--mid-blue)" stroke-width="1"/><path d="M3 5.2l1.4 1.4L7 3.8" fill="none" stroke="var(--mid-blue)" stroke-width="1.1"/></svg>Counter-ProductiveWorkBehaviours</div>
    </div>
  </div>

  <div class="footer">
    <svg width="520" height="36" viewBox="0 0 520 36">
      <rect width="520" height="36" fill="var(--navy)"/>
      <polygon points="0,0 300,0 318,36 0,36" fill="var(--mid-blue)"/>
    </svg>
    <span class="footer__cta">VISIT OUR WEBSITE FOR MORE INFORMATION</span>
    <span class="footer__url">www.torvenadvise.com.au</span>
  </div>
</section>

<!-- BACK PAGE -->
<section class="page page--back">
  <div class="header">
    <svg width="520" height="270" viewBox="0 0 520 270">
      <defs>
        <linearGradient id="photoBack" x1="0" y1="0" x2="1" y2="0">
          <stop offset="0" stop-color="var(--photo-b)"/>
          <stop offset=".6" stop-color="var(--photo-a)"/>
          <stop offset=".85" stop-color="#8a6a55"/>
          <stop offset="1" stop-color="var(--photo-a)"/>
        </linearGradient>
      </defs>
      <path d="M0 72 H520 V238 L310 262 L0 238 Z" fill="url(#photoBack)"/>
      <path d="M0 238 L310 262 L520 238 V243 L310 268 L0 243 Z" fill="var(--mid-blue)"/>
      <polygon points="258,0 520,0 520,76 258,76" fill="var(--white)"/>
      <polygon points="0,0 265,0 195,112 0,112" fill="var(--navy)"/>
      <polygon points="265,0 272,0 202,112 195,112" fill="var(--mid-blue)"/>
    </svg>
    <div class="photo-label" role="img" aria-label="Photo of a woman touching a glowing network of people and cloud icons over a night city"></div>
    <div class="brand brand--light">TORVEN<br>Consulting</div>
    <div class="title title--dark">Psychometric Assessments</div>
  </div>

  <div class="col col--left">
    <h3 class="h-sub">How do I access Psychometric Assessments?</h3>
    <p class="body">Psychometric Assessments are a powerful and cost-effective way of accurately predicting the likelihood of success of a candidate in any given role. In comparison to traditional recruitment and selection processes such as interviews and reference checking, Psychometric Assessment is evidence based, unbiased and incredibly accurate. The most accurate predictor of on the job success.</p>
  </div>
  <div class="col col--right">
    <h3 class="h-sub">How much do Psychometric Assessments cost?</h3>
    <p class="body">TORVEN offers a range of assessments and bundled assessments, with prices starting under $100 per assessment and even less for volume purchases.</p>
    <h3 class="h-sub" style="margin-top:8px">How can I buy Psychometric Assessments?</h3>
    <p class="body">Call the TORVEN Assessment Team on <b>1300 418 262</b> to discuss options and arrange set up.</p>
  </div>

  <div class="quote">
    <div class="quote__head"><span class="quote__mark">“</span>Testimonial</div>
    <p class="body">We recently asked one of our clients to tell us about their experience with the TORVEN Psychometric Assessments and how it has changed their recruitment process. This is what Dana Whitfield, General Manager – Human Resources at Harlow Grove Care said.</p>
    <ul>
      <li>30% decrease in advertising costs and agency fees</li>
      <li>The number of departures in the first year of service has decreased by 54% compared to the average of the six years prior.</li>
      <li>Instances of abandonment of employment in the first year of service have decreased by 61% compared to the same period.</li>
      <li>There have been no cases of permanent employees abandoning their employment in their first year since 2013 as opposed to 12 cases in the six years prior.</li>
      <li>In 2014 -2015, fewer staff than any year prior left with between 1 and 2 years service. Better retention has resulted in fewer employment vacancies over fiscal years 2014-2015 and 2015-2016, which equates to improved continuity of care for residents.</li>
      <li>The number of involuntary terminations in the first year of service has decreased by 83% compared to the six years prior to these changes.</li>
      <li>Since 2013 there has been only one termination due to performance within the first year, as opposed to 20 cases in the six years prior.</li>
      <li>Since July 2014 managers have rated 88% of their new employees as either “excellent” or “very good” after three months of work.</li>
      <li>Of the 46 instances of counselling or disciplinary action from 2013 to date, only six instances involved employees hired during this period. Employees hired since 2013 make up 48% of the current workforce but only 13% of the counselling or disciplinary cases.</li>
    </ul>
  </div>

  <div class="footer">
    <svg width="520" height="36" viewBox="0 0 520 36">
      <rect width="520" height="36" fill="var(--navy)"/>
      <polygon points="0,0 300,0 318,36 0,36" fill="var(--mid-blue)"/>
    </svg>
    <span class="footer__cta">VISIT OUR WEBSITE FOR MORE INFORMATION</span>
    <span class="footer__url">www.torvenadvise.com.au</span>
  </div>
</section>

</body>
</html>
```